GUMMY VORTEX BAG PACKAGE DESIGN

The FRONT of the label needs a fresh look. We are hoping for clean/modern.

The information on the label is correct

We would like to make CBD more prominent also. And we love showing that the product is made in Michigan , we have an icon you're welcome to move or make different.

I'm excited to see , thank you !

Target Market(s)

Adult, health supplement

```html
<!DOCTYPE html>
<html lang="en">
<head>
<meta charset="utf-8">
<title>VORTEX Butterfly Gummies – Front Label</title>
<link rel="stylesheet" href="https://fonts.googleapis.com/css2?family=Roboto:wght@400;700;900&family=Roboto+Condensed:wght@400;500&display=swap">
<style>
  :root {
    --page-bg: #ffffff;
    --pouch-black: #141414;
    --pouch-edge: #0a0a0a;
    --band-silver: #e4e4e4;
    --ink-dark: #111111;
    --ink-light: #f2f2f2;
    --brand-red: #d8232a;
  }
  * { margin: 0; padding: 0; box-sizing: border-box; }
  html, body {
    width: 1200px; height: 1039px; overflow: hidden;
    background: var(--page-bg);
  }
  .label {
    position: absolute;
    left: 295px; top: 110px;
    width: 610px; height: 810px;
    background: linear-gradient(100deg, var(--pouch-edge) 0%, var(--pouch-black) 40%, #1c1c1c 60%, var(--pouch-black) 100%);
    color: var(--ink-light);
    text-align: center;
    font-family: "Roboto", Arial, sans-serif;
  }
  .label > p, .label > h1 {
    position: absolute; left: 0; right: 0;
    line-height: 1; white-space: nowrap;
  }
  .count-band {
    position: absolute;
    right: 0; top: 48px;
    width: 268px; height: 74px;
    background: linear-gradient(90deg, #d6d6d6, var(--band-silver) 40%, #f4f4f4);
    border-radius: 37px 0 0 37px;
    color: var(--ink-dark);
    display: flex; align-items: center;
    padding-left: 6px;
  }
  .origin-badge { width: 64px; height: 64px; flex: none; }
  .count-copy { margin-left: 8px; text-align: left; }
  .count-row { display: flex; align-items: center; }
  .count-number { font-weight: 900; font-size: 48px; line-height: 1; letter-spacing: -1px; }
  .count-unit { font-weight: 900; font-size: 15px; line-height: 1.25; margin-left: 8px; }
  .count-note { font-family: "Roboto Condensed", Arial, sans-serif; font-weight: 500; font-size: 9.5px; margin-top: 3px; }
  .brand-name {
    top: 227px;
    font-weight: 900; font-size: 72px;
    color: var(--brand-red); letter-spacing: 1px;
  }
  .product-line {
    top: 312px;
    font-family: "Roboto Condensed", Arial, sans-serif;
    font-weight: 500; font-size: 28px; letter-spacing: 0.5px;
  }
  .hero-cbd {
    top: 373px;
    font-weight: 900; font-size: 108px; letter-spacing: 1px;
  }
  .hero-gummies {
    top: 468px;
    font-weight: 400; font-size: 60px;
  }
  .supplement-line {
    top: 539px;
    font-family: "Roboto Condensed", Arial, sans-serif;
    font-size: 24px; letter-spacing: 0.5px;
  }
  .dose-total {
    top: 625px;
    font-weight: 900; font-size: 62px;
  }
  .label > .dose-each {
    top: 681px;
    font-family: "Roboto Condensed", Arial, sans-serif;
    font-size: 14px; line-height: 1.3;
  }
  .net-weight {
    top: 770px;
    font-family: "Roboto Condensed", Arial, sans-serif;
    font-size: 21px;
  }
</style>
</head>
<body>
  <main class="label">
    <div class="count-band">
      <svg class="origin-badge" viewBox="0 0 64 64" aria-hidden="true">
        <circle cx="32" cy="32" r="30" fill="#f6f6f6" stroke="#444" stroke-width="1.5"/>
        <circle cx="32" cy="32" r="25" fill="none" stroke="#444" stroke-width="1"/>
      </svg>
      <div class="count-copy">
        <div class="count-row">
          <span class="count-number">20</span>
          <span class="count-unit">GUMMIES<br>PER PACK</span>
        </div>
        <div class="count-note">APPROX. (PACKAGED BY WEIGHT)</div>
      </div>
    </div>

    <h1 class="brand-name">KORVA'S</h1>
    <p class="product-line">BUTTERFLY GUMMIES</p>
    <p class="hero-cbd">CBD</p>
    <p class="hero-gummies">gummies</p>
    <p class="supplement-line">DIETARY SUPPLEMENT</p>
    <p class="dose-total">400mg</p>
    <p class="dose-each">APPROX. 20 <small>MG</small> CBD<br>PER BUTTERFLY</p>
    <p class="net-weight">NET WT. 2.47oz(70G)</p>
  </main>
</body>
</html>
```